Small business updating business cards

We have already updated our logo via Pixel Forum and downloaded it (hopefully) for you to use. Now an updated set of business cards for Neil Pollard and Stuart Pollard are also needed... we are also hoping that a copy of our outdated business card designs have uploaded successfully as Microsoft Publisher files. Our Strength Through Unity motto has died a slow death so we are hoping to remove it (and other superfluous lingo if the graphic covers the idea) and instead opt for a fancy graphic (?) on the second side of the card that really reflects our desire to obtain product / haulage from Road Transport / Yard Operators and convert legs of their haulage to rail freight where profitable (bulk haulage / containterised etc). Can you help us look larger, bolder and more robust than we really are (two man show)?
Target Market(s)
Transport Industry
Industry/Entity Type
Business
Contact Information for Business Card
Card details for both N Pollard and S Pollard have been uploaded on the publisher files
Colors
Designer to choose colors to be used in the design.
Requirements
Must have
- Similar theme both sides of card
Should not have
- Black on one side white on the other

```html
<!DOCTYPE html>
<html lang="en">
<head>
<meta charset="utf-8">
<title>Ironvale Freight – Business Card</title>
<link rel="stylesheet" href="https://fonts.googleapis.com/css2?family=Montserrat:ital,wght@0,700;1,400;1,700&display=swap">
<style>
  :root {
    --charcoal-deep: #2c2c2c;
    --brand-teal: #2484a0;
    --brand-gold: #c9a214;
    --brand-wordmark: #4f9a82;
    --text-white: #ffffff;
    --text-soft: #e8e8e8;
  }
  html, body {
    margin: 0;
    padding: 0;
    width: 1200px;
    height: 741px;
    overflow: hidden;
    background: var(--charcoal-deep);
  }
  .card {
    position: relative;
    width: 1200px;
    height: 741px;
    overflow: hidden;
    font-family: "Montserrat", Arial, sans-serif;
    color: var(--text-white);
  }
  .card__backdrop,
  .card__band-art {
    position: absolute;
    left: 0;
    top: 0;
    display: block;
  }
  .brand-name {
    position: absolute;
    left: 110px;
    top: 232px;
    margin: 0;
    font-weight: 700;
    font-size: 88px;
    line-height: 1;
    letter-spacing: -2px;
    color: var(--brand-wordmark);
    white-space: nowrap;
  }
  .tagline {
    position: absolute;
    left: 110px;
    top: 382px;
    margin: 0;
    font-style: italic;
    font-weight: 400;
    font-size: 23.5px;
    line-height: 35px;
    letter-spacing: 0.4px;
    color: var(--text-soft);
    text-transform: uppercase;
  }
  .contact-person {
    position: absolute;
    right: 77px;
    top: 490px;
    text-align right;
    text-align: right;
  }
  .contact-person__name {
    margin: 0;
    font-style: italic;
    font-weight: 700;
    font-size: 30px;
    line-height: 36px;
  }
  .contact-person__role {
    margin: 6px 0 0;
    font-style: italic;
    font-weight: 400;
    font-size: 22px;
    letter-spacing: 3px;
    color: var(--text-soft);
  }
  .contact-email {
    position: absolute;
    right: 74px;
    top: 660px;
    display: flex;
    align-items: center;
    gap: 18px;
    font-weight: 400;
    font-size: 24px;
    letter-spacing: 9px;
    color: var(--text-white);
  }
  .contact-email__icon { display: block; }
</style>
</head>
<body>
<div class="card">
  <svg class="card__backdrop" width="1200" height="741" viewBox="0 0 1200 741" aria-hidden="true">
    <defs>
      <linearGradient id="bg-base" x1="0" y1="0" x2="1" y2="1">
        <stop offset="0" stop-color="#3a3a3a"/>
        <stop offset="0.5" stop-color="#2f2f2f"/>
        <stop offset="1" stop-color="#2a2a2a"/>
      </linearGradient>
      <linearGradient id="bg-sweep" x1="1" y1="0" x2="0" y2="1">
        <stop offset="0" stop-color="#4a4a4a"/>
        <stop offset="1" stop-color="#333333"/>
      </linearGradient>
    </defs>
    <rect width="1200" height="741" fill="url(#bg-base)"/>
    <path d="M1165 0 C 1090 230, 900 430, 560 540 C 380 600, 200 660, 90 741 L1200 741 L1200 0 Z" fill="url(#bg-sweep)"/>
  </svg>

  <svg class="card__band-art" width="1200" height="741" viewBox="0 0 1200 741" role="img" aria-label="Sweeping gold and teal band artwork along the bottom edge">
    <defs>
      <linearGradient id="band-soft" x1="0" y1="0" x2="1" y2="0">
        <stop offset="0" stop-color="var(--brand-gold)"/>
        <stop offset="0.45" stop-color="var(--brand-teal)"/>
        <stop offset="1" stop-color="var(--brand-teal)"/>
      </linearGradient>
    </defs>
    <path d="M92 741 C 310 608, 700 562, 1200 585 L1200 741 Z" fill="url(#band-soft)"/>
  </svg>

  <h1 class="brand-name">Ironvale Freight</h1>

  <p class="tagline">Strategic alliance partners<br>providing logistical freight solutions</p>

  <div class="contact-person">
    <p class="contact-person__name">Stuart Pollard</p>
    <p class="contact-person__role">Director</p>
  </div>

  <div class="contact-email">
    <svg class="contact-email__icon" width="18" height="13" viewBox="0 0 18 13" aria-hidden="true">
      <rect x="0" y="0" width="18" height="13" fill="var(--text-white)"/>
      <polyline points="0.5,0.5 9,7 17.5,0.5" fill="none" stroke="var(--brand-teal)" stroke-width="1.5"/>
    </svg>
    <span>pollards@ironvalefreight.com.au</span>
  </div>
</div>
</body>
</html>
```